HOLTMARK Construction Services
Project: Stationary
Stationary
Simple
Derek Pannell
derek@hltservices-example.com
www.hltservices-example.com
Finalized Draft of the logo can be seen on the following URL: http://www.quillora-example.com/contests/business-logo-264. AI file will be uploaded soon. At the front of the business card the following text should be added design.engineer.build commercial.residential

```html
<!DOCTYPE html>
<html lang="en">
<head>
<meta charset="utf-8">
<title>HOLTMARK Construction Services – Business Cards</title>
<link rel="stylesheet" href="https://fonts.googleapis.com/css2?family=Arimo:wght@400;700&display=swap">
<style>
  :root {
    --bg: #2f2420;
    --card-top: #3d3d3d;
    --card-bottom: #1b1b1b;
    --text: #ffffff;
    --muted: #d6d6d6;
    --accent: #8cc63f;
    --band: #6a6a6a;
    --band-dark: #4e4e4e;
    --mark: #bdbdbd;
  }
  * { margin: 0; padding: 0; box-sizing: border-box; }
  html, body { width: 1200px; height: 945px; overflow: hidden; }
  body {
    background: var(--bg);
    position: relative;
    font-family: "Arimo", Arial, sans-serif;
    color: var(--text);
  }
  .card {
    position: absolute;
    width: 519px;
    height: 294px;
    border-radius: 10px;
    background: linear-gradient(160deg, var(--card-top), var(--card-bottom));
    box-shadow: 0 6px 18px rgba(0,0,0,.5);
    overflow: hidden;
  }
  .card-front { left: 89px; top: 166px; }
  .card-back { left: 592px; top: 480px; }

  .brand-dot {
    position: absolute;
    width: 76px; height: 76px;
    border-radius: 50%;
    background: var(--mark);
  }
  .brand-name {
    position: absolute;
    font-weight: 400;
    font-size: 34px;
    letter-spacing: 1px;
    color: var(--text);
    text-align: center;
    width: 260px;
    line-height: 38px;
  }
  .card-front .brand-dot { left: 110px; top: 40px; }
  .card-front .brand-name { left: 18px; top: 124px; }
  .services-line {
    position: absolute;
    left: 18px; top: 168px;
    width: 260px;
    text-align: center;
    font-size: 10.5px;
    letter-spacing: .5px;
    color: var(--accent);
    line-height: 14px;
  }

  .divider {
    position: absolute;
    left: 289px; top: 36px;
    width: 1px; height: 156px;
    background: linear-gradient(to bottom, transparent, #8a8a8a, transparent);
  }
  .person-name {
    position: absolute;
    left: 330px; top: 38px;
    font-size: 20px;
  }
  .contact {
    position: absolute;
    left: 330px; top: 158px;
    font-size: 11.5px;
    line-height: 15px;
    color: var(--muted);
    list-style: none;
    white-space: nowrap;
  }
  .services {
    position: absolute;
    left: 0; top: 237px;
    width: 100%; height: 42px;
    display: flex;
    background: linear-gradient(to bottom, var(--band), var(--band-dark));
  }
  .services li {
    list-style: none;
    flex: 1;
    display: flex; align-items: center; justify-content: center;
    font-size: 14px;
    color: var(--accent);
    text-transform: uppercase;
  }
  .services li + li { border-left: 1px solid #8e8e8e; }

  .card-back .brand-dot { left: 221px; top: 82px; }
  .card-back .brand-name { left: 130px; top: 170px; }
  .tagline {
    position: absolute;
    left: 0; top: 266px;
    width: 100%;
    text-align: center;
    font-size: 15px;
  }
</style>
</head>
<body>
  <section class="card card-front">
    <span class="brand-dot"></span>
    <div class="brand-name">HOLTMARK</div>
    <div class="services-line">design.engineer.build<br>commercial.residential</div>
    <span class="divider"></span>
    <div class="person-name">Derek Pannell</div>
    <ul class="contact">
      <li>555.014.2290</li>
      <li>www.hltservices-example.com</li>
      <li>derek@hltservices-example.com</li>
    </ul>
    <ul class="services">
      <li>Custom Homes</li>
      <li>Commercial</li>
      <li>Renovation</li>
    </ul>
  </section>

  <section class="card card-back">
    <span class="brand-dot"></span>
    <div class="brand-name">HOLTMARK</div>
    <div class="tagline">Building Modern Luxury.</div>
  </section>
</body>
</html>
```